Business card design needed

Family General Practitioner/ Family Physician.
Logo is the logo of the Crestmoor Guild of Family Clinicians Australia
http://kvplm.tarevo.edu.au/PictureGallery/logos/pages/CGFC%20logo_jpg.htm

Reason: Just a bit more time to make changes and the weekend for me to look at things closely and to choose. Thanks, Lumi

Thanks for all the submissions. So many of them are really works of art. Not one of them are not good. The ones that I am eliminating are the ones that I think are not suitable for me personally only, and because if I don't, it makes it very difficult to decide as many of you are also sending me slight variations of a card. I have just decided to choose a second place card too. Can't thank you all enough. Good luck, Lumi. P.S - Working today till 10 pm as the card says :-), so probably won't be able to give a feedback till late Saturday night or Sunday morning here in Sydney, Australia. 

Reason: Just added a second place to the budget and realised that Australia is ahead of the rest of the world in the time zone (only :-) - don't want to offend anyone or start a debate!! ) , so Monday deadline will mean it will be a weekend for the rest of the world. Just wanted to give everyone more time to submit their best, especially since I will be picking a second card too. Can't thank everyone enough for the submissions. P.S - Not keen on photos on the card.

Contact Information for Business Card

Dr. Lumi Harcourt M.B.B.S., F.C.G.F.C
Family General Practitioner
Address, timings, phone and fax number on the back.

Requirements
Must have
• Timings
Mon 7 am - 7 pm
Tues 7 am - 12 pm
Wed 7 am - 10 pm
Thurs 7 am - 12 pm
Fri 7 am - 8 pm
Sat 8 am - 10 pm
Sun - Off

```html
<!DOCTYPE html>
<html lang="en">
<head>
<meta charset="utf-8">
<title>Working Hours – Dr. Lumi Harcourt</title>
<link href="https://fonts.googleapis.com/css2?family=Roboto+Condensed:wght@400;700&display=swap" rel="stylesheet">
<style>
  :root {
    --page-bg: #ece5d2;
    --card-navy: #2b4263;
    --band-blue: #2e5380;
    --title-taupe: #a09479;
    --label-cream: #cfc6ad;
    --bar-orange: #f7931e;
  }
  * { margin: 0; padding: 0; box-sizing: border-box; }
  html, body {
    width: 1200px; height: 960px; overflow: hidden;
    background: var(--page-bg);
    font-family: "Roboto Condensed", "Arial Narrow", sans-serif;
  }
  .card {
    position: absolute; left: 138px; top: 220px;
    width: 924px; height: 520px;
    border-radius: 28px; overflow: hidden;
    background: var(--card-navy);
  }
  .card__title {
    position: absolute; top: 24px; left: 0; width: 100%;
    text-align: center; font-weight: 700; font-size: 31px;
    letter-spacing: 0.3px; color: var(--title-taupe);
  }
  .hours-axis span {
    position: absolute; top: 76px;
    font-size: 24px; color: var(--label-cream);
  }
  .day {
    position: absolute; left: 100px;
    font-size: 27px; color: var(--label-cream);
    line-height: 1;
  }
  .bar {
    position: absolute; height: 11px;
    background: var(--bar-orange);
  }
  .contact-band {
    position: absolute; left: 0; top: 413px;
    width: 100%; height: 107px;
    background: var(--band-blue);
  }
  .contact-band__address {
    position: absolute; top: 19px; left: 0; width: 100%;
    text-align: center; font-size: 24px; color: var(--label-cream);
  }
  .contact-band__line {
    position: absolute; top: 58px;
    font-size: 24px; color: var(--bar-orange);
  }
</style>
</head>
<body>
  <section class="card">
    <h1 class="card__title">WORKING HOURS</h1>

    <div class="hours-axis">
      <span style="left:306px">7A</span>
      <span style="left:338px">8A</span>
      <span style="left:465px">12P</span>
      <span style="left:688px">7P</span>
      <span style="left:720px">8P</span>
      <span style="left:783px">10P</span>
    </div>

    <div class="day" style="top:117px">Monday</div>
    <div class="bar" style="top:123px;left:306px;width:384px"></div>

    <div class="day" style="top:157px">Tuesday</div>
    <div class="bar" style="top:163px;left:306px;width:160px"></div>

    <div class="day" style="top:198px">Wednesday</div>
    <div class="bar" style="top:204px;left:306px;width:478px"></div>

    <div class="day" style="top:238px">Thursday</div>
    <div class="bar" style="top:244px;left:306px;width:160px"></div>

    <div class="day" style="top:279px">Friday</div>
    <div class="bar" style="top:285px;left:306px;width:415px"></div>

    <div class="day" style="top:319px">Saturday</div>
    <div class="bar" style="top:325px;left:338px;width:446px"></div>

    <div class="day" style="top:360px">Sunday</div>

    <footer class="contact-band">
      <p class="contact-band__address">Upper Level, Linden Court, Marrowfield Shopping Centre, Ashby Ridge, NSW 2190</p>
      <p class="contact-band__line" style="left:145px">PHONE: 02 7310 4400</p>
      <p class="contact-band__line" style="left:550px">FAX: 02 7310 4433</p>
    </footer>
  </section>
</body>
</html>
```